Packaging design for children’s shampoo bar

A design that could be used on solid shampoo and soap wraps then amended for jar labels. The packaging needs to be bright and child-friendly. We have a logo and a pattern, but please feel free to change them. I think it needs to be brighter.

I would like each product to have an accent colour and for the shampoo I am thinking of blue/teal. This will be complemented by the body wash bar (pink) and toothpaste (orange).

The shampoo bar wrap needs to contain the following information:

Pippa & Pals logo
Shampoo Bar
100% natural
Vegan & Palm Oil-Free
Weight 85 g
Made in the U.K.

Ingredients: sodium hydroxide, prunus amygdalus dulcis oil, olea europaea oil, cocos nucifera oil, ricinus communis seed oil, simmondsia chinensia seed oil.

Contact details: Pippa & Pals, Marden Oakley House, London N7 4QB. Website: www.Pippa and pals.co.U.K.

Brand board is here: https://www.filevaultex.com/s/k8rw2tqumezbvyx/Photo%2003-07-2020%2C%2021%2040%2034.jpg?dl=0

Inspiration is here: https://kitemoorstudio.co.uk/collections/beauty-grooming/products/dog-shampoo-100-natural-vegan

These are the wraps we shall be using: https://www.brightwickpress.co.uk/soap-wrap

Thank you so much for your interest in this project!

Target Market(s)

Children 5-12 years.

Requirements
Must have
• Clean design. Lots of white with bright colours.

```html
<!DOCTYPE html>
<html lang="en">
<head>
<meta charset="utf-8">
<title>Pippa &amp; Pals – Shampoo Bar Wrap</title>
<link href="https://fonts.googleapis.com/css2?family=Cabin+Sketch:wght@400;700&family=Cabin:wght@400&family=Gochi+Hand&family=Dancing+Script:wght@400&display=swap" rel="stylesheet">
<style>
  :root {
    --page: #ffffff;
    --wrap: #f1f1f1;
    --teal: #4a8590;
    --teal-soft: #9cc3c8;
    --ink: #1e1e1e;
    --green: #8aa83a;
    --sun: #f2dc3a;
    --turtle: #a9d3e6;
  }
  * { margin: 0; padding: 0; box-sizing: border-box; }
  html, body { width: 1200px; height: 1200px; overflow: hidden; background: var(--page); }
  .stage { position: relative; width: 1200px; height: 1200px; }
  .wrap {
    position: absolute;
    background: var(--wrap);
    border-radius: 12px;
    overflow: hidden;
  }
  .wrap--front { left: 216px; top: 81px; width: 744px; height: 507px; }
  .wrap--back  { left: 228px; top: 628px; width: 741px; height: 503px; }
  .abs { position: absolute; }

  /* Front */
  .brand-name {
    left: 96px; top: 70px;
    font-family: "Cabin", sans-serif;
    font-size: 44px; color: var(--teal); white-space: nowrap;
  }
  .turtle-art { left: 500px; top: 57px; width: 147px; height: 82px; border-radius: 50% 50% 20% 20%; background: linear-gradient(180deg, var(--turtle), #c7e3ef); }
  .title-big {
    font-family: "Cabin Sketch", sans-serif; font-weight: 700;
    color: var(--teal); line-height: 1; white-space: nowrap;
  }
  .title-shampoo { left: 102px; top: 170px; font-size: 122px; letter-spacing: 1px; }
  .title-bar { left: 455px; top: 293px; font-size: 124px; letter-spacing: 1px; }
  .hand-note { font-family: "Gochi Hand", cursive; font-size: 26px; color: var(--ink); white-space: nowrap; }
  .made-in { left: 98px; top: 334px; }
  .weight { left: 106px; top: 394px; }
  .divider-green { left: 93px; top: 381px; width: 200px; height: 3px; background: var(--green); border-radius: 2px; }
  .stamp { left: 309px; top: 306px; width: 132px; height: 132px; }
  .stamp-sun { left: 352px; top: 349px; width: 46px; height: 46px; border-radius: 50%; background: radial-gradient(circle, var(--sun) 40%, rgba(242,220,58,0.2) 70%); }

  /* Back */
  .natural-label { left: 0; width: 100%; top: 50px; text-align: center; font-family: "Gochi Hand", cursive; font-size: 27px; letter-spacing: 2px; color: #333; }
  .back-sun { left: 597px; top: 50px; width: 50px; height: 38px; border-radius: 50%; background: radial-gradient(circle, var(--sun) 35%, rgba(242,220,58,0.15) 70%); }
  .title-back { left: 0; width: 100%; top: 90px; text-align: center; font-size: 62px; letter-spacing: 1px; }
  .usage { left: 66px; top: 170px; width: 580px; font-family: "Cabin", sans-serif; font-size: 20px; line-height: 21px; color: var(--ink); }
  .usage em { font-family: "Dancing Script", cursive; font-style: normal; color: var(--teal); font-size: 21px; }
  .badges { left: 70px; top: 226px; width: 620px; display: flex; justify-content: space-between; list-style: none; }
  .badge { width: 92px; display: flex; flex-direction: column; align-items: center; }
  .badge-icon { width: 56px; height: 48px; border-radius: 12px; background: linear-gradient(180deg, #d7e8ea, #bcd8dc); }
  .badge-label { margin-top: 8px; font-family: "Dancing Script", cursive; font-size: 11px; color: var(--teal); white-space: nowrap; }
  .divider-dark { left: 403px; top: 318px; width: 282px; height: 3px; background: #222; border-radius: 2px; }
  .ingredients, .contact { font-family: "Cabin", sans-serif; font-size: 20px; line-height: 21px; color: var(--ink); }
  .ingredients { left: 64px; top: 322px; width: 310px; }
  .contact { left: 400px; top: 336px; font-style: normal; white-space: nowrap; }
  .flag { left: 622px; top: 356px; width: 62px; height: 32px; border-radius: 3px; background: linear-gradient(135deg, #1f3a8a 0 30%, #c8102e 30% 60%, #1f3a8a 60%); }
</style>
</head>
<body>
<main class="stage">

  <section class="wrap wrap--front" aria-label="Front of shampoo bar wrap">
    <div class="abs brand-name">Pippa &amp; Pals</div>
    <div class="abs turtle-art" role="img" aria-label="Illustration of a pale blue turtle"></div>
    <h1 class="abs title-big title-shampoo">SHAMPOO</h1>
    <div class="abs title-big title-bar">BAR</div>
    <p class="abs hand-note made-in">Made in the U.K.</p>
    <div class="abs divider-green"></div>
    <p class="abs hand-note weight">Weight 85 g</p>
    <svg class="abs stamp" viewBox="0 0 132 132" aria-label="100% natural, vegan, palm oil free">
      <defs><path id="stampRing" d="M66,66 m-50,0 a50,50 0 1,1 100,0 a50,50 0 1,1 -100,0"/></defs>
      <circle cx="66" cy="66" r="63" fill="none" stroke="#8aa83a" stroke-width="3"/>
      <text font-family="Gochi Hand, cursive" font-size="13" fill="#222" letter-spacing="1.5">
        <textPath href="#stampRing" startOffset="0">FREE - 100 % NATURAL - VEGAN - PALM OIL</textPath>
      </text>
    </svg>
    <div class="abs stamp-sun" role="img" aria-label="Hand-drawn yellow sun"></div>
  </section>

  <section class="wrap wrap--back" aria-label="Back of shampoo bar wrap">
    <p class="abs natural-label">100% NATURAL</p>
    <div class="abs back-sun" role="img" aria-label="Hand-drawn yellow sun"></div>
    <h2 class="abs title-big title-back">SHAMPOO BAR</h2>
    <p class="abs usage">Rub the bar between your hands creating a lather and apply to hair and massage, or apply bar directly to hair and massage. <em>Rinse!.</em></p>
    <ul class="abs badges">
      <li class="badge"><span class="badge-icon" role="img" aria-label="Leaf icon"></span><span class="badge-label">100% Natural</span></li>
      <li class="badge"><span class="badge-icon" role="img" aria-label="Vegetables icon"></span><span class="badge-label">Vegan</span></li>
      <li class="badge"><span class="badge-icon" role="img" aria-label="Rabbit icon"></span><span class="badge-label">No Animal Testing</span></li>
      <li class="badge"><span class="badge-icon" role="img" aria-label="Hand with heart icon"></span><span class="badge-label">Hand Made</span></li>
      <li class="badge"><span class="badge-icon" role="img" aria-label="Heart leaf icon"></span><span class="badge-label">Eco Friendly</span></li>
      <li class="badge"><span class="badge-icon" role="img" aria-label="Palm tree and drop icon"></span><span class="badge-label">Palm oil Free</span></li>
    </ul>
    <div class="abs divider-dark"></div>
    <p class="abs ingredients">Ingredients: sodium hydroxide, prunus amygdalus dulcis oil, olea europaea oil, cocos nucifera oil, ricinus communis seed oil, simmondsia chinensia seed oil.</p>
    <address class="abs contact">Pippa &amp; Pals<br>Marden Oakley House<br>London N7 4QB<br>www.Pippa and pals.co.U.K.</address>
    <div class="abs flag" role="img" aria-label="Brush-painted Union flag"></div>
  </section>

</main>
</body>
</html>
```